The Marmalade Reef

This is a whimsical Young Adult book about a moose in Africa who encounters a memorable cast of characters from around the world including a pirated cruise ship passenger, an African boy, a helicopter pilot, and more who want to help him escape a ruthless multi-millionaire hunter who is hellbent on killing him (the moose).

The name of the book is THE MARMALADE REEF
the subtitle is A TALE OF WANDERING MISHAPS

(that's a play on the name of the Skeleton Coast where the book takes place)

the author is Milo Venterbeck

Introduction by Trent Halvik
Harbor Ledger Weekly Bestselling Author

The final design should be graphic, whimsical, could feature any of the following imagery Moose, Banyan Tree, Dunes, Sun, Shipwreck. The type should be fun, energetic, colorful.
Updates

Hi all, I'm still waiting on the author who is out of the country and has limited access to email. One of these designs will be used for the cover, so no need to submit more. Thank you so much for sharing your talents.

Industry/Entity Type

Adult

```html
<!DOCTYPE html>
<html lang="en">
<head>
<meta charset="UTF-8">
<title>The Marmalade Reef — Cover</title>
<link rel="stylesheet" href="https://fonts.googleapis.com/css2?family=Amatic+SC:wght@400;700&family=Libre+Baskerville:wght@400;700&display=swap">
<style>
  :root {
    --backdrop: #ececec;
    --sand-light: #f7d9aa;
    --sand-deep: #e8b77c;
    --sea-light: #b5ecf1;
    --sea-mid: #3fd0dc;
    --sea-deep: #1fa2b0;
    --moose-brown: #7a5a42;
    --moose-tan: #b89a78;
    --star-red: #e0101e;
    --title-brown: #8a5a36;
    --tag-yellow: #fbe74d;
    --ink: #2b2420;
  }
  * { box-sizing: border-box; margin: 0; padding: 0; }
  html, body {
    width: 1200px; height: 1076px; overflow: hidden;
    background: var(--backdrop);
  }
  .cover {
    position: absolute; left: 300px; top: 58px;
    width: 600px; height: 960px; overflow: hidden;
    background: linear-gradient(180deg, var(--sand-light) 30%, var(--sand-deep) 100%);
    box-shadow: 0 18px 40px rgba(0,0,0,0.18);
  }
  .sea { position: absolute; left: 0; top: 0; width: 600px; height: 340px; }
  .moose-art {
    position: absolute; left: 10px; top: 170px; width: 430px; height: 460px;
    border-radius: 48% 52% 40% 44%;
    background: radial-gradient(ellipse at 50% 45%, var(--moose-tan) 0%, var(--moose-brown) 55%, rgba(122,90,66,0) 72%);
    opacity: 0.85;
  }
  .starfish-art {
    position: absolute; left: 360px; top: 462px; width: 62px; height: 58px;
    border-radius: 50%;
    background: var(--star-red);
  }
  .author-tag {
    position: absolute; right: 0; top: 64px;
    background: var(--tag-yellow); color: var(--ink);
    padding: 4px 16px 2px 26px;
    clip-path: polygon(14px 0, 100% 0, 100% 100%, 0 100%);
    font-family: "Amatic SC", cursive; font-weight: 700; font-size: 38px; letter-spacing: 1px;
  }
  .title {
    position: absolute; right: 30px; top: 440px; text-align: right;
    font-family: "Amatic SC", cursive; font-weight: 400; color: var(--title-brown);
    line-height: 0.98;
  }
  .title span { display: block; font-size: 104px; }
  .title .lead { font-size: 96px; }
  .subtitle {
    position: absolute; right: 24px; top: 858px;
    font-family: "Amatic SC", cursive; font-weight: 700; color: var(--title-brown);
    font-size: 30px; letter-spacing: 1px;
  }
  .intro-ribbon {
    position: absolute; left: 0; top: 698px; width: 290px; height: 132px;
    background: var(--tag-yellow);
    clip-path: polygon(0 0, 100% 0, 88% 50%, 100% 100%, 0 100%);
    padding: 16px 40px 0 14px; color: var(--ink);
    font-family: "Libre Baskerville", serif; text-align: center;
  }
  .intro-ribbon .intro { font-size: 15px; }
  .intro-ribbon .paper { font-size: 17px; font-weight: 700; margin-top: 12px; }
  .intro-ribbon .label { font-size: 11px; letter-spacing: 2px; margin-top: 8px; }
</style>
</head>
<body>
  <main class="cover">
    <svg class="sea" viewBox="0 0 600 340" role="img" aria-label="Illustrated ocean waves with two small trees on the horizon">
      <defs>
        <linearGradient id="seaTone" x1="0" y1="0" x2="0" y2="1">
          <stop offset="0" stop-color="var(--sea-light)"/>
          <stop offset="0.5" stop-color="var(--sea-mid)"/>
          <stop offset="1" stop-color="var(--sea-deep)"/>
        </linearGradient>
      </defs>
      <path d="M0 0 H600 V230 C520 200 460 250 380 250 C300 250 240 300 150 300 C90 300 40 320 0 335 Z" fill="url(#seaTone)"/>
    </svg>

    <div class="moose-art" role="img" aria-label="Illustrated moose walking across the sand"></div>
    <div class="starfish-art" role="img" aria-label="Small red starfish on the beach"></div>

    <div class="author-tag">Milo Venterbeck</div>

    <h1 class="title">
      <span class="lead">THE</span>
      <span>MARMALADE</span>
      <span>REEF</span>
    </h1>
    <p class="subtitle">A TALE OF WANDERING MISHAPS</p>

    <aside class="intro-ribbon">
      <p class="intro">Introduction by Trent Halvik</p>
      <p class="paper">Harbor Ledger Weekly</p>
      <p class="label">BESTSELLER</p>
    </aside>
  </main>
</body>
</html>
```